Healthcare technology company needs website design

We need a logo for a new company based in the U.S. We develop software to assist consumers identifying lowest cost healthcare coverage methods, including insurance, discount cards, and cash options. We would like to see designs that use multiple shades of green with the optional addition of other complimentary colors. The final design should communicate a unique blend of saving money while receiving the healthcare you need.
Need the following pages/sections: Homepage, Solutions, About Us, Contact
Competitors: www.velorinhealth.example; www.qdplm.example

Target Market(s)

Businesses

Industry/Entity Type

Healthcare

Coding

Coded - Design and coding required

Number of Pages Required

4 page

Colors
0054AA
0677BA
7BADD7
CADEEF
E8F1F8
00AB8E
00BBA5
67D7C9
C6EFE9
E9F9F6

Requirements
Must have
• Matching color theme with logo
Nice to have
• Animated background

```html
<!DOCTYPE html>
<html lang="en">
<head>
<meta charset="utf-8">
<title>Leafbridge Health – Healthcare Technology</title>
<link href="https://fonts.googleapis.com/css2?family=Montserrat:wght@400;500;600;700;900&family=Great+Vibes&display=swap" rel="stylesheet">
<style>
:root{
  --green:#2b9a3e;
  --green-dark:#1f8a33;
  --blue:#0677ba;
  --blue-deep:#0054aa;
  --blue-soft:#cadeef;
  --ink:#1d1d1d;
  --muted:#6b6b6b;
  --white:#ffffff;
  --page:#ffffff;
}
*{margin:0;padding:0;box-sizing:border-box}
html,body{width:1200px;height:4124px;overflow:hidden;background:var(--page)}
body{font-family:'Montserrat',sans-serif;color:var(--ink);position:relative}
.abs{position:absolute}
.section{position:absolute;left:0;width:1200px}

/* header */
.site-header{top:0;height:140px;background:var(--white)}
.brand{display:flex;align-items:center;gap:10px}
.brand-dot{width:34px;height:34px;border-radius:50%;background:var(--green)}
.brand-name{font-weight:700;color:var(--green);font-size:21px;letter-spacing:.5px;line-height:1}
.nav a{position:absolute;top:64px;font-size:12px;color:#444;text-decoration:none;letter-spacing:.3px}
.nav .active{left:388px;top:57px;width:65px;height:30px;border:1.5px solid var(--green);border-radius:3px;display:flex;align-items:center;justify-content:center;color:var(--green)}
.header-divider{left:778px;top:56px;width:1px;height:30px;background:#ddd}
.contact-item{top:63px;font-size:11.5px;color:#333;display:flex;align-items:center;gap:10px}
.header-rule{top:138px;height:7px;background:var(--green)}

/* hero */
.hero{top:145px;height:645px;background:linear-gradient(100deg,#e9edf2 0%,#dfe6ee 40%,#c9c2b0 70%,#b8a88a 100%)}
.hero-script{left:88px;top:130px;font-family:'Great Vibes',cursive;font-size:90px;color:var(--green);line-height:1}
.hero-title{left:88px;top:228px;font-size:78px;font-weight:900;color:var(--blue);letter-spacing:1px;line-height:1}
.hero-sub{left:90px;top:338px;font-size:25px;font-weight:500;color:#1e1e1e}
.hero-text{left:90px;top:393px;width:470px;font-size:13.5px;line-height:25px;color:#7a7a7a}
.btn{display:flex;align-items:center;justify-content:center;font-size:12px;font-weight:600;letter-spacing:.6px;border-radius:4px;text-decoration:none}
.btn-solid{background:var(--green);color:var(--white)}
.btn-outline{border:1.5px solid var(--green);color:var(--green);background:var(--white)}
.btn-light{border:2px solid var(--white);color:var(--white)}

/* common headings */
.eyebrow{font-size:16px;font-weight:600;color:var(--green)}
.heading{font-weight:900;color:var(--blue);font-size:44px;letter-spacing:.5px;line-height:1}
.copy{font-size:12.5px;line-height:21px;color:#666}

/* solutions */
.solutions{top:1443px;height:732px;background:linear-gradient(180deg,#0a73c2,#0667b3)}
.sol-card{top:260px;width:331px;height:290px;background:var(--white);border-radius:4px;text-align:center}
.sol-icon{position:absolute;left:110px;top:34px;width:112px;height:112px;border-radius:50%;background:var(--green-dark)}
.sol-title{position:absolute;left:0;right:0;top:160px;font-size:22px;font-weight:500;color:#222}
.sol-text{position:absolute;left:55px;right:55px;top:206px;font-size:12.5px;line-height:21px;color:#777}

/* blogs */
.blog-card{top:2410px;width:446px;height:407px;background:var(--white);box-shadow:0 6px 24px rgba(0,0,0,.08)}
.blog-tag{height:29px;background:var(--green);color:var(--white);font-size:15px;font-weight:600;padding:4px 0 0 50px;border-radius:3px 3px 0 0}
.blog-img{height:185px}
.blog-text{position:absolute;left:52px;top:234px;width:350px;font-size:12px;line-height:21px;color:#666}
.blog-meta{position:absolute;top:361px;font-size:10.5px;color:var(--green);display:flex;align-items:center;gap:6px}

/* join band */
.join{top:3502px;height:250px;background:linear-gradient(90deg,#2e9c3f,#3aa34a 55%,#2b9339)}
</style>
</head>
<body>

<header class="section site-header">
  <div class="abs brand" style="left:90px;top:50px">
    <span class="brand-dot"></span>
    <span class="brand-name">LEAFBRIDGE HEALTH</span>
  </div>
  <nav class="nav">
    <a class="active" href="#">HOME</a>
    <a href="#" style="left:478px">ABOUT US</a>
    <a href="#" style="left:578px">SOLUTIONS</a>
    <a href="#" style="left:687px">CONTACT</a>
  </nav>
  <div class="abs header-divider"></div>
  <div class="abs contact-item" style="left:829px">
    <svg width="20" height="14" viewBox="0 0 20 14"><rect width="20" height="14" rx="1" fill="#0677ba"/><path d="M1 1l9 7 9-7" stroke="#fff" stroke-width="1.6" fill="none"/></svg>
    info@leafbridge.example
  </div>
  <div class="abs contact-item" style="left:992px">
    <svg width="18" height="18" viewBox="0 0 24 24"><path d="M6.6 10.8a15 15 0 006.6 6.6l2.2-2.2c.3-.3.7-.4 1-.2 1.1.4 2.3.6 3.6.6.6 0 1 .4 1 1V20c0 .6-.4 1-1 1A17 17 0 013 4c0-.6.4-1 1-1h3.5c.6 0 1 .4 1 1 0 1.3.2 2.5.6 3.6.1.3 0 .7-.2 1z" fill="#0677ba"/></svg>
    +1 555 0100 209
  </div>
</header>
<div class="section abs header-rule"></div>

<section class="section hero">
  <div role="img" aria-label="Photo of a dental professional in mask and safety glasses" class="abs" style="left:620px;top:0;width:580px;height:645px;background:linear-gradient(90deg,rgba(220,225,232,0),#c9b78f 60%,#d8c49a)"></div>
  <div class="abs hero-script">Healthcare</div>
  <h1 class="abs hero-title">TECHNOLOGY</h1>
  <p class="abs hero-sub">Low Cost Healthcare Coverage Methods</p>
  <p class="abs hero-text">Lorem ipsum dolor sit amet, consectetur adipiscing elitrutrum urna fermentum sem egestas condimentum.</p>
  <a class="abs btn btn-solid" href="#" style="left:90px;top:475px;width:166px;height:56px">VIEW DETAILS</a>
</section>

<section class="section" style="top:790px;height:653px">
  <div role="img" aria-label="Medical team photo in a green and blue tint" class="abs" style="left:115px;top:122px;width:322px;height:366px;border-radius:6px;background:linear-gradient(135deg,#56a56a,#2f8e4b 60%,#4a9ed0)"></div>
  <p class="abs eyebrow" style="left:566px;top:135px">Who We Are</p>
  <h2 class="abs heading" style="left:564px;top:165px">ABOUT THE FIRM</h2>
  <p class="abs copy" style="left:566px;top:247px;width:510px">Lorem ipsum dolor sit amet, consectetur adipiscing elit. Etiam rutrum urna fermentum sem egestas condimentum. Nulla tristique nisi et sem facilisis porttitor. Quisque tincidunt volutpat erat ac semper. Donec euismod rutrum nisi ac aliquet. Mauris scelerisque arcu ac ultricies consectetur.</p>
  <p class="abs copy" style="left:566px;top:352px;width:510px">Aliquam purus libero, maximus faucibus pretium at, rhoncus at lectus. Proin vestibulum vel massa a pellentesque. Nullam id tortor ut nisi viverra.</p>
  <a class="abs btn btn-outline" href="#" style="left:566px;top:433px;width:167px;height:56px">VIEW DETAILS</a>
</section>

<section class="section solutions">
  <div role="img" aria-label="Blue tinted photo of a stethoscope" class="abs" style="left:0;top:0;width:1200px;height:732px;background:radial-gradient(ellipse at 60% 40%,rgba(255,255,255,.08),rgba(0,0,0,0) 60%)"></div>
  <p class="abs" style="left:0;width:1190px;top:101px;text-align:center;color:#fff;font-size:16px;font-weight:600">Medically Recognized Offers</p>
  <h2 class="abs heading" style="left:0;width:1190px;top:130px;text-align:center;color:#fff">OUR SOLUTIONS</h2>

  <div class="abs sol-card" style="left:80px">
    <div class="sol-icon"><svg viewBox="0 0 112 112" width="112" height="112"><path d="M56 62c-10-8-16-13-16-20a8 8 0 0116-3 8 8 0 0116 3c0 7-6 12-16 20z" fill="#fff"/><path d="M30 58c6 10 14 18 22 22M82 58c-6 10-14 18-22 22" stroke="#fff" stroke-width="6" fill="none" stroke-linecap="round"/></svg></div>
    <h3 class="sol-title">Insurance</h3>
    <p class="sol-text">Lorem ipsum dolor sit amet, consect etur adipiscing elit.</p>
  </div>
  <div class="abs sol-card" style="left:430px">
    <div class="sol-icon"><svg viewBox="0 0 112 112" width="112" height="112"><circle cx="66" cy="40" r="14" fill="none" stroke="#fff" stroke-width="4"/><text x="66" y="46" text-anchor="middle" font-family="Montserrat,sans-serif" font-size="16" font-weight="700" fill="#fff">%</text><rect x="24" y="62" width="10" height="22" fill="#fff"/><path d="M36 64h20c6 0 6 6 0 6h-8M36 82h24l22-16c4-3 0-8-4-6l-14 8" stroke="#fff" stroke-width="5" fill="none" stroke-linejoin="round"/></svg></div>
    <h3 class="sol-title">Discount Cards</h3>
    <p class="sol-text">Lorem ipsum dolor sit amet, consect etur adipiscing elit.</p>
  </div>
  <div class="abs sol-card" style="left:780px">
    <div class="sol-icon"><svg viewBox="0 0 112 112" width="112" height="112"><rect x="26" y="36" width="58" height="34" rx="3" fill="none" stroke="#fff" stroke-width="5"/><rect x="34" y="44" width="50" height="34" rx="3" fill="#1f8a33" stroke="#fff" stroke-width="5"/><circle cx="59" cy="61" r="7" fill="#fff"/></svg></div>
    <h3 class="sol-title">Cash Options</h3>
    <p class="sol-text">Lorem ipsum dolor sit amet, consect etur adipiscing elit.</p>
  </div>

  <svg class="abs" style="left:570px;top:627px" width="74" height="40" viewBox="0 0 74 40"><path d="M22 4L8 20l14 16M52 4l14 16-14 16" stroke="#fff" stroke-width="2.5" fill="none"/></svg>
</section>

<section class="section" style="top:2175px;height:695px">
  <p class="abs eyebrow" style="left:0;width:1208px;top:126px;text-align:center">Latest From Blogs</p>
  <h2 class="abs heading" style="left:0;width:1208px;top:152px;text-align:center">OFFERS OF HELP</h2>
</section>

<article class="abs blog-card" style="left:127px">
  <div class="blog-tag">Daily Structure - Work</div>
  <div class="blog-img" role="img" aria-label="Close-up photo of a stethoscope held in hand" style="background:linear-gradient(90deg,#d8c1b3,#e9ddd6 50%,#b9b3ae)"></div>
  <p class="blog-text">Donec consectetur blandit sem faucibus dignissim. Interdum et malesuada fames ac ante ipsum primis in faucibu sellus tincidunt</p>
  <span class="blog-meta" style="left:213px"><svg width="14" height="14" viewBox="0 0 14 14"><circle cx="7" cy="7" r="5.5" fill="none" stroke="#2b9a3e"/></svg>2 Comments</span>
  <span class="blog-meta" style="left:329px"><svg width="14" height="14" viewBox="0 0 14 14"><circle cx="7" cy="4.5" r="3" fill="none" stroke="#2b9a3e"/><path d="M1.5 13c1-4 10-4 11 0" fill="none" stroke="#2b9a3e"/></svg>By Marek</span>
</article>
<article class="abs blog-card" style="left:640px">
  <div class="blog-tag">Administrative Support</div>
  <div class="blog-img" role="img" aria-label="Portrait photo of a clinician in dark scrubs against a concrete wall" style="background:linear-gradient(90deg,#7c7f81,#5a5d60 50%,#8a8c8e)"></div>
  <p class="blog-text">Donec consectetur blandit sem faucibus dignissim. Interdum et malesuada fames ac ante ipsum primis in faucibu sellus tincidunt</p>
  <span class="blog-meta" style="left:220px"><svg width="14" height="14" viewBox="0 0 14 14"><circle cx="7" cy="7" r="5.5" fill="none" stroke="#2b9a3e"/></svg>2 Comments</span>
  <span class="blog-meta" style="left:336px"><svg width="14" height="14" viewBox="0 0 14 14"><circle cx="7" cy="4.5" r="3" fill="none" stroke="#2b9a3e"/><path d="M1.5 13c1-4 10-4 11 0" fill="none" stroke="#2b9a3e"/></svg>By Marek</span>
</article>

<section class="section" style="top:2870px;height:632px">
  <div role="img" aria-label="Photo of a smiling patient in a blue t-shirt with arms crossed" class="abs" style="left:150px;top:15px;width:390px;height:617px;border-radius:180px 180px 0 0;background:linear-gradient(180deg,#c7b49f 0%,#8a94b8 45%,#5c6f9f 100%)"></div>
  <h2 class="abs heading" style="left:627px;top:188px">TESTIMONIALS</h2>
  <p class="abs" style="left:627px;top:280px;width:440px;font-size:15.5px;line-height:32px;color:#666">Nulla vel ex malesuada elit eleifend tincidunt sed venenatis leo. Praesent et lorem dignissim elit faucibus cursus. Phasellus eu ipsum</p>
  <p class="abs" style="left:627px;top:408px;font-size:22px;font-weight:500;color:#222">R. Calder <span style="font-size:15px;color:var(--blue);margin-left:6px">- Patient</span></p>
  <svg class="abs" style="left:1010px;top:400px" width="42" height="32" viewBox="0 0 42 32"><path d="M4 0h14v14c0 9-5 15-14 18l-2-5c5-2 7-5 7-9H4zM24 0h14v14c0 9-5 15-14 18l-2-5c5-2 7-5 7-9h-5z" fill="#2b9a3e"/></svg>
</section>

<section class="section join">
  <div role="img" aria-label="Green tinted photo of medical equipment" class="abs" style="left:0;top:0;width:1200px;height:250px;background:radial-gradient(ellipse at 70% 80%,rgba(255,255,255,.1),rgba(0,0,0,0) 60%)"></div>
  <p class="abs" style="left:133px;top:64px;color:#fff;font-size:16px;font-weight:600">We are looking for a new team member!</p>
  <h2 class="abs heading" style="left:133px;top:93px;color:#fff;font-size:38px">WOULD YOU LIKE TO JOIN US?</h2>
  <p class="abs" style="left:135px;top:147px;width:440px;color:#fff;font-size:12.5px;line-height:21px">Lorem ipsum dolor sit amet, consectetur adipiscing elim rutrum urna fermentum sem egestas condimentum.</p>
  <a class="abs btn btn-light" href="#" style="left:913px;top:98px;width:167px;height:54px">CONTACT US</a>
</section>

<footer class="section" style="top:3752px;height:372px">
  <div class="abs brand" style="left:130px;top:118px">
    <span class="brand-dot"></span>
    <span class="brand-name">LEAFBRIDGE HEALTH</span>
  </div>
  <p class="abs" style="left:135px;top:193px;font-size:12px;line-height:25px;color:#555">Leafbridge Health<br>Suite 12 - 4500 USA<br>contact@leafbridge.example</p>
  <h4 class="abs" style="left:540px;top:125px;font-size:16px;font-weight:600">Quick Links</h4>
  <ul class="abs" style="left:540px;top:168px;list-style:none;font-size:12px;line-height:31px;color:#555">
    <li><span style="color:var(--blue);margin-right:8px">→</span>HOME</li>
    <li><span style="color:var(--blue);margin-right:8px">→</span>WHAT WE CAN</li>
    <li><span style="color:var(--blue);margin-right:8px">→</span>CONTACT</li>
    <li><span style="color:var(--blue);margin-right:8px">→</span>OFFERS OF HELP</li>
  </ul>
  <h4 class="abs" style="left:873px;top:125px;font-size:16px;font-weight:600">Copyright</h4>
  <p class="abs" style="left:834px;top:172px;font-size:12px;color:#555">© 2022 Leafbridge Health</p>
  <div class="abs" style="left:873px;top:211px;display:flex;gap:12px">
    <span style="width:22px;height:22px;border-radius:50%;background:var(--blue)"></span>
    <span style="width:22px;height:22px;border-radius:50%;background:var(--blue)"></span>
    <span style="width:22px;height:22px;border-radius:50%;background:var(--blue)"></span>
  </div>
  <div class="abs" style="left:0;top:358px;width:1200px;height:14px;background:var(--blue)"></div>
</footer>

</body>
</html>
```